New letter head for Air Conditioning business

We need a new professional letter head design to suit our new re-branded air conditioning business. Our new logo is attached

```html
<!DOCTYPE html>
<html lang="en">
<head>
<meta charset="utf-8">
<title>Veltra Letterhead</title>
<link href="https://fonts.googleapis.com/css2?family=Poppins:ital,wght@0,400;0,500;0,600;1,400&display=swap" rel="stylesheet">
<style>
  :root {
    --backdrop: #e3e4e4;
    --paper: #ffffff;
    --ink: #3a3a3c;
    --body-grey: #7a7a7a;
    --green: #5dbf84;
    --coral: #ef6b5e;
    --charcoal: #3b3b3d;
    --white: #ffffff;
  }
  html, body {
    margin: 0;
    width: 1200px;
    height: 900px;
    overflow: hidden;
    background: var(--backdrop);
    font-family: "Poppins", sans-serif;
  }
  .letterhead {
    position: absolute;
    left: 300px;
    top: 26px;
    width: 600px;
    height: 848px;
    background: var(--paper);
    box-shadow: 0 10px 30px rgba(0,0,0,0.12);
  }
  .brand {
    position: absolute;
    left: 48px;
    top: 48px;
    display: flex;
    align-items: center;
    gap: 12px;
  }
  .brand-dot {
    width: 34px;
    height: 34px;
    border-radius: 50%;
    background: var(--green);
  }
  .brand-name {
    font-weight: 600;
    font-size: 24px;
    letter-spacing: 3px;
    color: var(--ink);
    line-height: 1;
  }
  .salutation {
    position: absolute;
    left: 48px;
    top: 282px;
    font-size: 13px;
    font-weight: 500;
    color: var(--body-grey);
    margin: 0;
  }
  .letter-date {
    position: absolute;
    right: 48px;
    top: 300px;
    font-size: 10px;
    font-style: italic;
    color: var(--body-grey);
    margin: 0;
  }
  .letter-body {
    position: absolute;
    left: 48px;
    right: 48px;
    top: 322px;
  }
  .letter-body p {
    margin: 0 0 14px;
    font-size: 10px;
    line-height: 15px;
    color: var(--body-grey);
    text-align: justify;
  }
  .closing {
    position: absolute;
    left: 48px;
    top: 624px;
    font-size: 13px;
    font-weight: 500;
    color: var(--body-grey);
    margin: 0;
  }
  .signature {
    position: absolute;
    left: 46px;
    top: 652px;
    width: 110px;
    height: 42px;
    background: linear-gradient(90deg, #ececec, #f6f6f6);
  }
  .footer {
    position: absolute;
    left: 0;
    bottom: 18px;
    width: 600px;
    height: 52px;
  }
  .footer-band { position: absolute; left: 0; top: 0; }
  .footer-contact {
    position: absolute;
    left: 40px;
    top: 9px;
    font-size: 10px;
    line-height: 17px;
    color: var(--white);
  }
  .footer-line { display: flex; align-items: center; gap: 6px; }
  .footer-icon { flex: none; display: block; }
  .footer-divider {
    position: absolute;
    left: 190px;
    top: 12px;
    width: 1px;
    height: 28px;
    background: var(--coral);
  }
  .footer-address {
    position: absolute;
    left: 206px;
    top: 9px;
    font-size: 10px;
    line-height: 17px;
    color: var(--white);
  }
  .footer-mark {
    position: absolute;
    left: 364px;
    top: 10px;
    width: 32px;
    height: 32px;
    border-radius: 50%;
    background: var(--green);
  }
  .footer-web {
    position: absolute;
    left: 440px;
    top: 18px;
    font-size: 10px;
    line-height: 17px;
    color: var(--white);
    display: flex;
    align-items: center;
    gap: 6px;
  }
</style>
</head>
<body>
  <main class="letterhead">
    <header class="brand">
      <div class="brand-dot"></div>
      <div class="brand-name">VELTRA</div>
    </header>

    <p class="salutation">Dear Harwell,</p>
    <p class="letter-date">30 January 2080</p>

    <section class="letter-body">
      <p>Lorem ipsum dolor sit amet, consectetuer adipiscing elit, sed diam nonummy nibh euismod tincidunt ut laoreet dolore magna aliquam erat volutpat. Ut wisi enim ad minim commodo consequat. Duis dolore te feugait nulla facilisi. Nam liber tempor cum soluta nobis eleifendu Lorem ipsum dolor sit amet, consectetuer adipiscing elit, sed diam nonummy nibh euismod consequat. Duis dolore te feugait nulla facilisi. Nam liber tempor cum soluta nobis eleifendu euismod tincidunt ut laoreet dolore magna aliquam erat volutpat. Ut wisi enim ad minimoa</p>
      <p>Consectetuer adipiscing elit, sed diam nonummy nibh euismod tincidunt utom laoreet dolore magna aliquam erat volutpat. Ut wisi enim ad minim veniam, quis nostrud exercilmo Consectetuer adipiscing elit, sed diam nonummy nibh euismod tincidunt utom laoreet dolore magna aliquam erat volutpat. Ut wisi enim ad minim veniam, quis nostrud exerci tation ullamcorper nisl suscipit lobortis nisl utiliomu aliquip ex ea commod uconse qualitmu</p>
      <p>tincidunt ut laoreet dolore magna aliquam erat volutpat. Ut wisi enim ad minim commodo consequat. Duis dolore te feugait nulla facilisi. Nam liber tempor cum soluta nobis eleifendu Lorem ipsum dolor sit amet, consectetuer adipiscing elit, sed diam nonummy nibh euismod tincidunt ut laoreet dolore magna aliquam erat volutpat. Ut wisi enim ad minim commodnconsequat. Duis dolore te feugait nulla facilisi. Nam liber tempor cum soluta nobineleifendu euismod tincidunt ut laoreet dolore magna aliquam erat volutpat. Ut wisims</p>
    </section>

    <p class="closing">Sincerely Yours</p>
    <div class="signature" role="img" aria-label="Handwritten signature"></div>

    <footer class="footer">
      <svg class="footer-band" width="600" height="52" viewBox="0 0 600 52" aria-hidden="true">
        <polygon points="0,0 350,0 366,26 350,52 0,52" fill="#3b3b3d"/>
        <polygon points="412,0 600,0 600,52 412,52 398,26" fill="#ef6b5e"/>
      </svg>
      <div class="footer-contact">
        <div class="footer-line">
          <svg class="footer-icon" width="9" height="9" viewBox="0 0 24 24" aria-hidden="true"><path fill="#5dbf84" d="M6.6 10.8a15 15 0 0 0 6.6 6.6l2.2-2.2a1 1 0 0 1 1-.25 11.4 11.4 0 0 0 3.6.57 1 1 0 0 1 1 1V20a1 1 0 0 1-1 1A17 17 0 0 1 3 4a1 1 0 0 1 1-1h3.5a1 1 0 0 1 1 1c0 1.25.2 2.45.57 3.57a1 1 0 0 1-.25 1z"/></svg>
          <span>000 000-0000</span>
        </div>
        <div class="footer-line">
          <svg class="footer-icon" width="9" height="9" viewBox="0 0 24 24" aria-hidden="true"><rect x="2" y="5" width="20" height="14" fill="#5dbf84"/><path d="M2 5l10 8 10-8" stroke="#3b3b3d" stroke-width="2" fill="none"/></svg>
          <span>info@anydomain.com</span>
        </div>
      </div>
      <div class="footer-divider"></div>
      <div class="footer-address">PO Box 8800 Subville St00<br>Sample City Country 6103</div>
      <div class="footer-mark"></div>
      <div class="footer-web">
        <svg class="footer-icon" width="9" height="9" viewBox="0 0 24 24" aria-hidden="true"><circle cx="12" cy="12" r="10" fill="#ffffff"/><path d="M2 12h20M12 2c3 3 3 17 0 20M12 2c-3 3-3 17 0 20" stroke="#ef6b5e" stroke-width="1.6" fill="none"/></svg>
        <span>www.anydomain.com</span>
      </div>
    </footer>
  </main>
</body>
</html>
```